Fahrzeugbeschriftung für Industriemaler-Unternehmen
Tolle Designer und sehr geduldig.
Zielgruppe
Wir sind Industriemaler Unternehmen und suchen ein hochwertiges und elegantes Design, unsere Zielgruppen sind allgemein in der Industrie Branche tätig, wie z. B. Medizinischer- und Technischer Gerätebau. Dazu gehören technische Kunststoffteile, Präzisionteile, Kleinmaschinen, Messgeräte, usw.
Aufgabenstellung
Das Design sollte präzis, elegant und Modern sein. Farbenkombination sollte mit Schwarzer Hintergrund sein, da unsere Fahrzeuge Schwarz sind. Wir sind in einem 2 sprachigen Standort tätig, daher sollte der design Deutsch und Französisch sein. Damit Sie einen besseren Überblick haben, können Sie gerne unsere Webseite anschauen. Als Bildmaterial haben wir nur unseren Logo.
Horizon Laque Atelier Sàrl
Birkenweg 14b
2563 Ipsach
info@laqueatelier-exemple.ch
www.laqueatelier-exemple.ch

```html
<!DOCTYPE html>
<html lang="fr">
<head>
<meta charset="utf-8">
<title>Horizon Laque Atelier – Fahrzeugbeschriftung</title>
<link rel="stylesheet" href="https://fonts.googleapis.com/css2?family=Rajdhani:wght@500&family=Montserrat:wght@700&display=swap">
<style>
  :root {
    --backdrop: #e6e8ec;
    --wrap-black: #0b0b0c;
    --text-light: #e9e9ea;
    --splash-red: #e5303a;
    --splash-orange: #f18a21;
    --splash-yellow: #e4d81e;
    --splash-green: #4cc46a;
    --splash-blue: #2f6fd0;
    --splash-magenta: #d8338f;
    --splash-teal: #3bbf9a;
  }
  html, body {
    margin: 0;
    width: 1200px;
    height: 800px;
    overflow: hidden;
    background: linear-gradient(180deg, #f2f3f5 0%, var(--backdrop) 100%);
  }
  .canvas {
    position: relative;
    width: 1200px;
    height: 800px;
  }
  .wrap-panel {
    position: absolute;
    left: 120px;
    top: 180px;
    width: 990px;
    height: 340px;
    background: var(--wrap-black);
    border-radius: 22px;
    overflow: hidden;
  }
  .arch-bands {
    position: absolute;
    left: 0;
    top: 0;
    width: 990px;
    height: 340px;
  }
  .arch-bands .stop-magenta { stop-color: var(--splash-magenta); }
  .arch-bands .stop-yellow { stop-color: var(--splash-yellow); }
  .arch-bands .stop-green { stop-color: var(--splash-green); }
  .arch-bands .stop-blue { stop-color: var(--splash-blue); }
  .arch-bands .stop-orange { stop-color: var(--splash-orange); }
  .arch-bands .stop-red { stop-color: var(--splash-red); }
  .arch-bands .stop-teal { stop-color: var(--splash-teal); }
  .mascot-art {
    position: absolute;
    left: 66px;
    top: 6px;
    width: 184px;
    height: 166px;
    border-radius: 48% 52% 40% 60% / 50% 45% 55% 50%;
    background: linear-gradient(120deg, var(--splash-red) 0%, var(--splash-orange) 22%, var(--splash-yellow) 40%, var(--splash-blue) 62%, #8fd43a 82%, #6fcc2c 100%);
  }
  .brand {
    position: absolute;
    left: 237px;
    top: 166px;
    font-family: "Rajdhani", sans-serif;
    font-weight: 500;
    color: var(--text-light);
    line-height: 1;
  }
  .brand__name {
    display: block;
    font-size: 42px;
    letter-spacing: -0.5px;
  }
  .brand__trade {
    display: block;
    margin-top: 2px;
    font-size: 18.5px;
    letter-spacing: 0.2px;
  }
  .contact {
    position: absolute;
    margin: 0;
    font-family: "Montserrat", sans-serif;
    font-weight: 700;
    font-style: normal;
    color: var(--text-light);
    white-space: nowrap;
  }
  .contact--address {
    right: 318px;
    top: 205px;
    text-align: right;
    font-size: 8.6px;
    line-height: 11.5px;
  }
  .contact--email {
    left: 258px;
    top: 280px;
    font-size: 12.5px;
  }
  .contact--web {
    left: 500px;
    top: 285px;
    font-size: 12.5px;
  }
</style>
</head>
<body>
<main class="canvas">
  <section class="wrap-panel" aria-label="Seitenansicht der Fahrzeugbeschriftung">
    <svg class="arch-bands" viewBox="0 0 990 340" role="img" aria-label="Farbspritzer in Regenbogentönen über den Radläufen">
      <defs>
        <linearGradient id="rearArch" x1="20" y1="0" x2="244" y2="0" gradientUnits="userSpaceOnUse">
          <stop offset="0" class="stop-magenta"/>
          <stop offset="0.3" class="stop-yellow"/>
          <stop offset="0.6" class="stop-blue"/>
          <stop offset="0.85" class="stop-orange"/>
          <stop offset="1" class="stop-red"/>
        </linearGradient>
        <linearGradient id="frontArch" x1="708" y1="0" x2="928" y2="0" gradientUnits="userSpaceOnUse">
          <stop offset="0" class="stop-magenta"/>
          <stop offset="0.25" class="stop-green"/>
          <stop offset="0.5" class="stop-blue"/>
          <stop offset="0.75" class="stop-orange"/>
          <stop offset="1" class="stop-teal"/>
        </linearGradient>
      </defs>
      <path class="arch arch--rear" fill="url(#rearArch)" d="M22 320 A110 110 0 0 1 242 320 L218 320 A86 86 0 0 0 46 320 Z"/>
      <path class="arch arch--front" fill="url(#frontArch)" d="M708 320 A110 110 0 0 1 928 320 L904 320 A86 86 0 0 0 732 320 Z"/>
    </svg>
    <div class="mascot-art" role="img" aria-label="Illustration: farbenfrohes Reptil in Regenbogenfarben"></div>
    <div class="brand">
      <span class="brand__name">horizon</span>
      <span class="brand__trade">LAQUE ATELIER</span>
    </div>
    <address class="contact contact--address">
      Horizon Laque Atelier Sàrl<br>
      Birkenweg 14b<br>
      2563 Ipsach
    </address>
    <p class="contact contact--email">info@laqueatelier-exemple.ch</p>
    <p class="contact contact--web">www.laqueatelier-exemple.ch</p>
  </section>
</main>
</body>
</html>
```